Plateau UI App Design

We need to have a proper design for a web app that we currently mocked in Powerpoint (will be provided). This PPT contains about 15 slides. The final app will have about 5-6 screens but with context sensitive elements. we would prefer a workflow based UI, i.e. screens should not be clogged but the interface should behave like a wizard or an QX Plateau UI app.

- Design should be flat and should be Plateau UI / Quilt Style (using this as a design language and tiles / colors)
- The final result has to be much more designed, modern and homogeneous than now.
- We would also need a clickable HTML(5) prototype of the design, please let us know how this can be achieved
- Internet connection does not matter for the project, so has to work just within a browser but does not need to connect to a server (could even be local files)
- This does not need to be a fully functional HTML 5 page, after all it is a prototype / screen design, so it would be more like mouse over / clicking / moving to next screen
- If you cannot deliver HTML5 then please suggest providing something that we can edit easily ourselves (e.g. a Powerpoint again)
- TROVE is the name of our product

Target Market(s)

Financial institutions

Industry/Entity Type

Internet

Requirements
Must have
• Plateau UI / Quilt design

```html
<!DOCTYPE html>
<html lang="en">
<head>
<meta charset="utf-8">
<title>TROVE – Golden Price</title>
<link href="https://fonts.googleapis.com/css2?family=Open+Sans:wght@400;600;700&display=swap" rel="stylesheet">
<style>
  :root {
    --page-bg: #26374d;
    --panel-bg: #ffffff;
    --header-bg: #3b4148;
    --brand-bg: #2c3137;
    --header-divider: #50575f;
    --header-text: #e6e9ec;
    --header-sub: #aab1b8;
    --tile-bg: #f6f7f8;
    --tile-border: #d8dcdf;
    --tile-text: #4a4f55;
    --accent: #4ab4dd;
    --heading: #4f555b;
    --label-bg: #678c9b;
    --label-text: #ffffff;
    --value-bg: #f8f9fa;
    --value-text: #4c7686;
    --row-line: #e3e7ea;
    --chart-line: #2f3942;
    --chart-fill: #eef2f5;
    --chart-grid: #cfd6db;
    --chart-axis: #7b858e;
  }
  * { box-sizing: border-box; margin: 0; padding: 0; }
  html, body { width: 1200px; height: 985px; overflow: hidden; }
  body {
    background: var(--page-bg);
    font-family: "Open Sans", Arial, sans-serif;
    position: relative;
  }
  .app {
    position: absolute; left: 128px; top: 100px;
    width: 943px; height: 778px;
    background: var(--panel-bg);
    box-shadow: 0 10px 40px rgba(0,0,0,.35);
  }
  .app-header {
    position: absolute; left: 0; top: 0; width: 100%; height: 59px;
    background: var(--header-bg);
  }
  .brand {
    position: absolute; left: 0; top: 0; width: 148px; height: 59px;
    background: var(--brand-bg);
    display: flex; align-items: center; justify-content: center;
    color: #ffffff; font-weight: 700; font-size: 24px; letter-spacing: 1px;
  }
  .header-item { position: absolute; top: 0; height: 59px; display: flex; align-items: center; }
  .header-item svg { width: 34px; height: 34px; stroke: var(--header-text); fill: none; stroke-width: 1.6; }
  .header-text { margin-left: 15px; font-size: 13.5px; line-height: 21px; }
  .header-title { color: var(--header-text); font-weight: 600; }
  .header-sub { color: var(--header-sub); }
  .header-divider { position: absolute; top: 6px; width: 1px; height: 47px; background: var(--header-divider); }

  .tile {
    position: absolute; top: 82px; width: 125px; height: 101px;
    background: var(--tile-bg); border: 1px solid var(--tile-border); border-radius: 2px;
    display: flex; flex-direction: column; align-items: center; justify-content: flex-end;
    padding-bottom: 14px; color: var(--tile-text); font-size: 16px;
  }
  .tile svg { width: 46px; height: 46px; margin-bottom: 9px; fill: none; stroke: var(--tile-text); stroke-width: 1.6; }
  .tile.is-active { background: var(--accent); border-color: var(--accent); color: #ffffff; }
  .tile.is-active svg { stroke: #ffffff; }

  .section-title {
    position: absolute; display: flex; align-items: center;
    font-size: 19px; font-weight: 600; color: var(--heading);
  }
  .section-title svg { width: 28px; height: 28px; margin-left: 8px; fill: none; stroke: var(--heading); stroke-width: 1.5; }

  .data-table { position: absolute; left: 35px; width: 450px; border-collapse: collapse; font-size: 14.5px; }
  .data-table td { height: 36px; padding-left: 15px; border-bottom: 1px solid var(--row-line); }
  .data-table .label { width: 224px; background: var(--label-bg); color: var(--label-text); border-bottom-color: rgba(255,255,255,.25); }
  .data-table .value { background: var(--value-bg); color: var(--value-text); border-right: 1px solid var(--row-line); }
  .data-table tr:first-child td.value { border-top: 1px solid var(--row-line); }

  .history-quote { position: absolute; left: 556px; top: 282px; font-size: 13px; font-weight: 600; color: var(--heading); }
  .history-chart { position: absolute; left: 508px; top: 308px; width: 408px; height: 204px; overflow: visible; }
  .history-chart text { font-family: "Open Sans", Arial, sans-serif; }
</style>
</head>
<body>
<main class="app">
  <header class="app-header">
    <div class="brand">TROVE</div>

    <div class="header-item" style="left:184px">
      <svg viewBox="0 0 34 34"><path d="M3 31h28M6 30V22h4v8M13 30V18h4v12M20 30V14h4v16M27 30V9h4v21"/><path d="M5 17l8-6 6 3 12-9"/></svg>
      <div class="header-text">
        <div class="header-title">NORVALE CORP 1.25% SR NTS 02/06/17</div>
        <div class="header-sub">NVC17A &nbsp;|&nbsp; CXSE &nbsp;|&nbsp; Corporate Bond</div>
      </div>
    </div>
    <span class="header-divider" style="left:496px"></span>

    <div class="header-item" style="left:529px">
      <svg viewBox="0 0 34 34"><rect x="2" y="9" width="30" height="21" rx="2"/><path d="M12 9V5h10v4M2 17h30M15 17v3h4v-3"/></svg>
      <div class="header-text">
        <div class="header-title">Fixed Income</div>
        <div class="header-sub">Portfolio</div>
      </div>
    </div>
    <span class="header-divider" style="left:707px"></span>

    <div class="header-item" style="left:754px">
      <svg viewBox="0 0 34 34"><path d="M11 13H6v18h22V13h-5M17 3v19M11 9l6-6 6 6"/></svg>
      <div class="header-text">
        <div class="header-title">Export</div>
        <div class="header-sub">12/03/2015 &nbsp;&nbsp; 18:02</div>
      </div>
    </div>
  </header>

  <nav>
    <div class="tile is-active" style="left:35px">
      <svg viewBox="0 0 46 46"><circle cx="23" cy="23" r="20"/><path d="M28 16c-1-2-3-3-5-3-3 0-5 2-5 4 0 6 11 3 11 9 0 3-3 4-6 4-2 0-4-1-5-3M23 10v26"/></svg>
      Golden Price
    </div>
    <div class="tile" style="left:222px">
      <svg viewBox="0 0 46 46"><rect x="11" y="5" width="31" height="22" rx="2"/><rect x="5" y="12" width="31" height="24" rx="2" fill="var(--tile-bg)"/><path d="M10 36v8M6 40h8"/></svg>
      Requests
    </div>
    <div class="tile" style="left:410px">
      <svg viewBox="0 0 46 46"><circle cx="23" cy="23" r="20"/><path d="M28 16c-1-2-3-3-5-3-3 0-5 2-5 4 0 6 11 3 11 9 0 3-3 4-6 4-2 0-4-1-5-3M23 10v26"/></svg>
      Silver Copies
    </div>
    <div class="tile" style="left:596px">
      <svg viewBox="0 0 46 46"><rect x="4" y="4" width="38" height="38" rx="3"/><path d="M13 23l7 7 13-14"/></svg>
      Plausibility
    </div>
    <div class="tile" style="left:785px">
      <svg viewBox="0 0 46 46"><path d="M23 3l4 3 5-1 2 5 5 2-1 5 3 4-3 4 1 5-5 2-2 5-5-1-4 3-4-3-5 1-2-5-5-2 1-5-3-4 3-4-1-5 5-2 2-5 5 1z"/><path d="M16 35l-2 10 6-3 3 4M30 35l2 10-6-3-3 4"/></svg>
      Policy
    </div>
  </nav>

  <h2 class="section-title" style="left:35px;top:233px">Golden Price
    <svg viewBox="0 0 28 28"><circle cx="14" cy="14" r="12"/><path d="M17 9.5c-.6-1-1.7-1.6-3-1.6-1.8 0-3 1-3 2.3 0 3.6 6.5 1.8 6.5 5.4 0 1.6-1.6 2.5-3.5 2.5-1.3 0-2.5-.6-3.1-1.7M14 6v16"/></svg>
  </h2>
  <table class="data-table" style="top:274px">
    <tr><td class="label">Price Value</td><td class="value">187,24</td></tr>
    <tr><td class="label">Currency</td><td class="value">USD</td></tr>
    <tr><td class="label">Price Date</td><td class="value">10.03.2014</td></tr>
    <tr><td class="label">Quotation Type</td><td class="value">Official Close</td></tr>
    <tr><td class="label">Market</td><td class="value">CXSE</td></tr>
    <tr><td class="label">Data Source</td><td class="value">Ledgerline</td></tr>
    <tr><td class="label">Price Unit</td><td class="value">Piece</td></tr>
    <tr><td class="label">IFRS 13</td><td class="value">Level 1</td></tr>
  </table>

  <h2 class="section-title" style="left:35px;top:584px">Pricing Policy
    <svg viewBox="0 0 28 28"><circle cx="14" cy="10" r="7"/><path d="M10 16l-2 10 6-3 6 3-2-10"/></svg>
  </h2>
  <table class="data-table" style="top:624px">
    <tr><td class="label">Pricing Policy</td><td class="value">Standard EOD</td></tr>
    <tr><td class="label">Pricing Method</td><td class="value">US Bonds</td></tr>
  </table>

  <h2 class="section-title" style="left:516px;top:231px">History</h2>
  <div class="history-quote">187.24 &nbsp;+0.87 (0.47%)</div>
  <svg class="history-chart" viewBox="530 340 340 170" role="img" aria-label="Price history line chart, Monday to Friday">
    <g stroke="var(--chart-grid)" stroke-width="0.8" stroke-dasharray="3 2">
      <line x1="574" y1="353" x2="860" y2="353"/>
      <line x1="574" y1="375" x2="860" y2="375"/>
      <line x1="574" y1="397" x2="860" y2="397"/>
      <line x1="574" y1="418" x2="860" y2="418"/>
      <line x1="574" y1="440" x2="860" y2="440"/>
      <line x1="574" y1="461" x2="860" y2="461"/>
    </g>
    <path d="M574 353 C600 370 620 370 646 375 C680 380 690 418 717 418 C745 418 760 397 789 397 C825 397 835 353 860 353 L860 482 L574 482 Z" fill="var(--chart-fill)"/>
    <g stroke="#a9b8c3" stroke-width="0.8">
      <line x1="574" y1="353" x2="574" y2="482"/>
      <line x1="646" y1="375" x2="646" y2="482"/>
      <line x1="717" y1="418" x2="717" y2="482"/>
      <line x1="789" y1="397" x2="789" y2="482"/>
      <line x1="860" y1="353" x2="860" y2="482"/>
      <line x1="574" y1="482" x2="860" y2="482"/>
    </g>
    <path d="M574 353 C600 370 620 370 646 375 C680 380 690 418 717 418 C745 418 760 397 789 397 C825 397 835 353 860 353" fill="none" stroke="var(--chart-line)" stroke-width="1.6"/>
    <g fill="#ffffff" stroke="var(--chart-line)" stroke-width="1.3">
      <circle cx="574" cy="353" r="3"/><circle cx="646" cy="375" r="3"/><circle cx="717" cy="418" r="3"/><circle cx="789" cy="397" r="3"/><circle cx="860" cy="353" r="3"/>
    </g>
    <g fill="#a9b8c3">
      <circle cx="574" cy="482" r="1.5"/><circle cx="646" cy="482" r="1.5"/><circle cx="717" cy="482" r="1.5"/><circle cx="789" cy="482" r="1.5"/><circle cx="860" cy="482" r="1.5"/>
    </g>
    <circle cx="789" cy="377" r="11" fill="var(--accent)"/>
    <path d="M785 386 L789 391 L793 386 Z" fill="var(--accent)"/>
    <text x="789" y="380.5" font-size="8" font-weight="700" fill="#ffffff" text-anchor="middle">60+</text>
    <g font-size="8" fill="var(--chart-axis)" text-anchor="end">
      <text x="549" y="356">60</text><text x="549" y="399">40</text><text x="549" y="442">20</text><text x="547" y="485">0</text>
    </g>
    <g font-size="8" fill="var(--chart-axis)" text-anchor="middle">
      <text x="574" y="502">Mon</text><text x="646" y="502">Tue</text><text x="717" y="502">Wed</text><text x="789" y="502">Thu</text><text x="860" y="502">Fri</text>
    </g>
  </svg>
</main>
</body>
</html>
```